we are a mobile auto windscreen replacement business we are looking for a smart, stylish designed card on a matte black base color with large metallic silver KVT (similar to the zenpod box)
over the whole face of the card but down the bottom have (your local automotive & machinery glass specialist) & over the back

Reason: I'm looking for a design like no other something that really wows people to grab a card & use my business

Target Market(s)

Adults in western countries that own an automotive fleet company or anybody that owns a car

Industry/Entity Type

Automotive

Contact Information for Business Card

front: KVTglassworks
Back: MORRIS 0482 65 71 93 Abn: 52840193657
morris@kvtglassworks.com.au & www.kvtglassworks.com.au

Logo styles of interest
Lettermark Logo
Requirements
Must have
• Metallic font on matte background
Nice to have
• 3D font that's glass or the word KVT smashed into glass on a black background I've added some pictures that maybe you could incorporate in the background or font it would be great to see a professionals ideas

```html
<!DOCTYPE html>
<html lang="en">
<head>
<meta charset="utf-8">
<title>KVT Glassworks — Business Card</title>
<link rel="stylesheet" href="https://fonts.googleapis.com/css2?family=Cinzel:wght@400;600;700&family=Roboto+Condensed:wght@700&family=Noto+Sans:wght@400&display=swap">
<style>
  :root {
    --backdrop: #9c9b98;
    --card-black: #0b0b0b;
    --card-edge: #050505;
    --watermark: #171717;
    --silver: #cfe3ec;
    --rule: #8fb8c8;
    --cyan: #62d2f6;
  }
  * { margin: 0; padding: 0; box-sizing: border-box; }
  html, body {
    width: 1200px; height: 1200px; overflow: hidden;
    background: var(--backdrop);
  }
  .sheet {
    width: 1200px; height: 1200px;
    display: flex; flex-direction: column; align-items: center; justify-content: center;
    gap: 60px;
  }
  .card {
    position: relative;
    width: 820px; height: 500px;
    background: radial-gradient(ellipse at 50% 40%, #141414 0%, var(--card-black) 70%);
    border: 1px solid var(--card-edge);
    overflow: hidden;
    box-shadow: 0 10px 26px rgba(0,0,0,0.35);
  }
  .card__watermark {
    position: absolute; inset: 0;
    display: flex; align-items: center; justify-content: center;
    font-family: "Roboto Condensed", sans-serif; font-weight: 700;
    font-size: 430px; letter-spacing: -6px; line-height: 1;
    color: var(--watermark);
    user-select: none;
  }
  .front__brand {
    position: absolute; left: 0; right: 0; top: 200px;
    text-align: center;
    font-family: "Cinzel", serif; font-weight: 600;
    font-size: 64px; letter-spacing: 2px;
    color: var(--silver);
  }
  .back__identity {
    position: absolute; left: 0; right: 0; top: 160px;
    text-align: center;
  }
  .back__name {
    display: inline-block;
    font-family: "Cinzel", serif; font-weight: 700;
    font-size: 62px; letter-spacing: 3px; line-height: 1;
    color: var(--silver);
    padding: 0 18px 8px;
    border-bottom: 2px solid var(--rule);
  }
  .back__tagline {
    margin-top: 6px;
    font-family: "Cinzel", serif; font-weight: 400;
    font-size: 13px; letter-spacing: 0.5px;
    color: var(--silver);
  }
  .back__numbers {
    position: absolute; left: 40px; top: 290px;
    font-family: "Noto Sans", sans-serif; font-size: 26px; line-height: 1.3;
    color: var(--cyan);
  }
  .back__online {
    position: absolute; right: 40px; top: 370px;
    text-align: right;
    font-family: "Noto Sans", sans-serif; font-size: 26px; line-height: 1.3;
    color: var(--cyan);
  }
</style>
</head>
<body>
<main class="sheet">
  <section class="card card--front" aria-label="Card front">
    <div class="card__watermark" aria-hidden="true">KVT</div>
    <div class="front__brand">KVT</div>
  </section>

  <section class="card card--back" aria-label="Card back">
    <div class="card__watermark" aria-hidden="true">KVT</div>
    <div class="back__identity">
      <div class="back__name">MORRIS</div>
      <div class="back__tagline">Automotive and Machinery Glass Specialist</div>
    </div>
    <div class="back__numbers">
      <p class="back__phone">0482 65 71 93</p>
      <p class="back__abn">ABN 52840193657</p>
    </div>
    <div class="back__online">
      <p class="back__web">www.kvtglassworks.com.au</p>
      <p class="back__email">morris@kvtglassworks.com.au</p>
    </div>
  </section>
</main>
</body>
</html>
```